Resume build

I need someone to develop a resume for me. This needs to include a stylized template as well as improving the content of my existing resume.
Updates

All content generated. Just need resume to be formatted and stylized a few different options. With offer a few different head shots to go into it as well. Final versions to be in PDF.

Target Market(s)

this is not for finding a job but is for presenting to clients on who I am and why I'm the qualified candidate to perform their work.

Industry/Entity Type

Marine

Colors
0054AA
0677BA
7BADD7
CADEEF
E8F1F8

Requirements
Must have
• must be in PDF and have a location to add a picture later in the top corner

```html
<!DOCTYPE html>
<html lang="en">
<head>
<meta charset="utf-8">
<title>Rowan Calder – Resume</title>
<link href="https://fonts.googleapis.com/css2?family=Poppins:wght@300;400;500;600;700&display=swap" rel="stylesheet">
<style>
  :root {
    --navy: #0054AA;
    --teal: #1F88B9;
    --sky: #CCEAF9;
    --paper: #FFFFFF;
    --backdrop: #F1F1F1;
    --ink: #444A52;
    --ink-soft: #5A6068;
    --accent: #1A7DB8;
    --portrait: #7C8085;
  }
  * { box-sizing: border-box; margin: 0; padding: 0; }
  html, body {
    width: 1200px; height: 840px; overflow: hidden;
    background: var(--backdrop);
    font-family: "Poppins", sans-serif;
  }
  .resume {
    position: absolute; left: 316px; top: 20px;
    width: 567px; height: 800px;
    background: var(--sky);
    box-shadow: 0 6px 24px rgba(0,0,0,0.12);
    overflow: hidden;
  }
  .header {
    position: absolute; left: 0; top: 0; width: 100%; height: 211px;
    background: var(--navy);
  }
  .name {
    position: absolute; left: 35px; top: 46px;
    font-size: 41px; font-weight: 700; color: #fff; letter-spacing: 0.3px;
  }
  .title-band {
    position: absolute; left: 35px; top: 133px; width: 400px; height: 40px;
    background: var(--teal);
    color: #fff; font-size: 11px; font-weight: 400; letter-spacing: 2.4px;
    line-height: 40px; padding-left: 21px;
  }
  .portrait {
    position: absolute; left: 380px; top: 32px; width: 150px; height: 150px;
    border-radius: 50%; border: 1.5px solid #1b1b1b;
    background: radial-gradient(circle at 50% 40%, #9A9EA3 0%, var(--portrait) 55%, #F4F4F4 56%, #FFFFFF 100%);
  }
  .panel { position: absolute; }
  .panel--side { left: 35px; width: 195px; background: var(--teal); color: #fff; padding: 28px 23px 0 25px; }
  .panel--main { left: 249px; width: 286px; background: var(--paper); padding: 28px 24px 0 31px; }
  .panel--top { top: 227px; height: 347px; }
  .panel--bottom { top: 591px; height: 179px; }
  .heading {
    font-size: 11.5px; font-weight: 600; letter-spacing: 1.4px; text-transform: uppercase;
  }
  .panel--main .heading { color: var(--ink); }
  .profile-text {
    margin-top: 13px; font-size: 7.6px; line-height: 12.7px; letter-spacing: 0.6px; font-weight: 300;
  }
  .skills-heading { margin-top: 37px; }
  .skills { list-style: none; margin-top: 17px; }
  .skills li {
    display: flex; justify-content: space-between;
    font-size: 7.6px; letter-spacing: 0.6px; font-weight: 300; height: 22.7px;
  }
  .contact { list-style: none; margin-top: 18px; }
  .contact li {
    display: flex; align-items: flex-start; gap: 10px;
    font-size: 6.4px; font-weight: 300; line-height: 9px; margin-bottom: 15px;
  }
  .contact svg { flex: 0 0 8px; width: 8px; height: 8px; margin-top: 1px; }
  .contact .email { text-decoration: underline; }
  .timeline { list-style: none; margin-top: 17px; padding-left: 20px; }
  .timeline li { position: relative; }
  .timeline li::before {
    content: ""; position: absolute; left: -20px; top: 3px;
    width: 5px; height: 5px; border-radius: 50%; background: var(--accent);
  }
  .timeline li:not(:last-child)::after {
    content: ""; position: absolute; left: -18.5px; top: 16px; bottom: 8px;
    width: 1px; background: var(--accent);
  }
  .job { padding-bottom: 21px; }
  .job-date { font-size: 7.6px; color: var(--ink); letter-spacing: 0.6px; }
  .job-role { margin-top: 5px; font-size: 7.8px; font-weight: 600; color: var(--accent); letter-spacing: 0.8px; }
  .job-text { margin-top: 5px; font-size: 7.4px; line-height: 12.7px; color: var(--ink-soft); letter-spacing: 0.6px; font-weight: 300; }
  .edu { padding-left: 22px; margin-top: 19px; }
  .edu li { padding-bottom: 19px; }
  .edu li::before { left: -22px; top: 2px; }
  .edu li:not(:last-child)::after { left: -20.5px; top: 13px; bottom: 14px; }
  .edu-title { font-size: 9.8px; font-weight: 600; color: var(--accent); }
  .edu-meta { margin-top: 4px; font-size: 7.4px; color: var(--ink-soft); letter-spacing: 0.8px; }
</style>
</head>
<body>
<main class="resume">
  <header class="header">
    <h1 class="name">Rowan Calder</h1>
    <div class="title-band">MARINE PROJECT OPERATIONS MANAGER</div>
    <div class="portrait" role="img" aria-label="Headshot photo placeholder"></div>
  </header>

  <section class="panel panel--side panel--top">
    <h2 class="heading">Profile</h2>
    <p class="profile-text">My job at this company and I best teacher alnguage is to make a check on a company system from a client.</p>
    <h2 class="heading skills-heading">My Skills</h2>
    <ul class="skills">
      <li><span>Gemany Language</span><span>70%</span></li>
      <li><span>English Language</span><span>85%</span></li>
      <li><span>Spain Language</span><span>90%</span></li>
      <li><span>American Language</span><span>75%</span></li>
      <li><span>Chniese Language</span><span>80%</span></li>
      <li><span>Japanese Language</span><span>80%</span></li>
    </ul>
  </section>

  <section class="panel panel--main panel--top">
    <h2 class="heading">Work Experience</h2>
    <ul class="timeline">
      <li class="job">
        <div class="job-date">2015 - 2017</div>
        <div class="job-role">Language Teacher in School A</div>
        <p class="job-text">My job at this company is to make a check on a company system from a client and fix if there is a malfunction in the system.</p>
      </li>
      <li class="job">
        <div class="job-date">2017 - 2019</div>
        <div class="job-role">Language Teacher in School B</div>
        <p class="job-text">My job at this company is to make a check on a company system from a client and fix if there is a malfunction in the system.</p>
      </li>
      <li class="job">
        <div class="job-date">2019 - 2022</div>
        <div class="job-role">Language Teacher in School C</div>
        <p class="job-text">My job at this company is to make a check on a company system from a client and fix if there is a malfunction in the system.</p>
      </li>
    </ul>
  </section>

  <section class="panel panel--side panel--bottom">
    <h2 class="heading">Contact</h2>
    <ul class="contact">
      <li>
        <svg viewBox="0 0 24 24" fill="#fff"><path d="M6.6 10.8a15.1 15.1 0 0 0 6.6 6.6l2.2-2.2c.3-.3.7-.4 1-.2 1.1.4 2.3.6 3.6.6.6 0 1 .4 1 1V20c0 .6-.4 1-1 1A17 17 0 0 1 3 4c0-.6.4-1 1-1h3.5c.6 0 1 .4 1 1 0 1.3.2 2.5.6 3.6.1.3 0 .7-.2 1z"/></svg>
        <span>1 (555) 014 2290</span>
      </li>
      <li>
        <svg viewBox="0 0 24 24" fill="#fff"><path d="M2 5h20v14H2z M2 5l10 8 10-8" stroke="#1F88B9" stroke-width="1.6"/></svg>
        <span class="email">rowan@tidelinemarine.com</span>
      </li>
      <li>
        <svg viewBox="0 0 24 24" fill="#fff"><path d="M12 2a7 7 0 0 0-7 7c0 5.2 7 13 7 13s7-7.8 7-13a7 7 0 0 0-7-7zm0 9.5a2.5 2.5 0 1 1 0-5 2.5 2.5 0 0 1 0 5z"/></svg>
        <span>42 Harbourview Lane • Port Elden Canada • K0A 1B2</span>
      </li>
    </ul>
  </section>

  <section class="panel panel--main panel--bottom">
    <h2 class="heading">Educations</h2>
    <ul class="timeline edu">
      <li>
        <div class="edu-title">2011 - 2013 in Edu University</div>
        <div class="edu-meta">Teacher Major | GPA : 3.79</div>
      </li>
      <li>
        <div class="edu-title">2013 - 2015 in Edu University</div>
        <div class="edu-meta">Teacher Major | GPA : 3.66</div>
      </li>
    </ul>
  </section>
</main>
</body>
</html>
```